Building showcase catalogue for a post frame construction company

We are looking for a brochure for our clients showcasing our buildings. We are a post frame building company that makes commercial, ag, homes, and other building types. We are looking for a brochure that we can use with all the types of buildings simply by changing out the pictures. We would like a more photo heavy brochure thats 1-5 pages. We want the design to feel high end luxury. Our colors are black, white, and chrome. I will upload our logo as well as some building photos in the suburban category of our buildings. We would like a page to showcase some building layouts as well.

We need the size to be us letter size.

Industry/Entity Type

Construction

Font styles to use
Serif

Colors

Designer to choose only greyscale colors for use in the design.

Requirements
Must have
• A space to showcase building photos, small text space for information. An area to showcase building layouts.
Nice to have
• I would like to have a very clean professional look thats looks high end.
Should not have
• Areas for detail pictures. We mostly have exterior building shots.

```html
<!DOCTYPE html>
<html lang="en">
<head>
<meta charset="utf-8">
<title>Post Frame Building – Catalogue Spreads</title>
<link href="https://fonts.googleapis.com/css2?family=Playfair+Display:wght@900&family=Crimson+Pro:wght@400;600&display=swap" rel="stylesheet">
<style>
  :root{
    --ink:#1c1c1c;
    --charcoal:#3b3b3b;
    --steel-light:#efefef;
    --steel-mid:#cfcfcf;
    --steel-dark:#a9a9a9;
    --paper:#ffffff;
    --caption:#2a2a2a;
    --frame:#9a9a9a;
  }
  *{box-sizing:border-box;margin:0;padding:0}
  html,body{width:714px;height:1200px;overflow:hidden;background:var(--paper)}
  body{position:relative;font-family:"Crimson Pro",Georgia,serif;color:var(--ink)}

  .page{position:absolute;width:279px;height:361px;overflow:hidden;
    background:linear-gradient(90deg,#c9c9c9 0%,#f4f4f4 22%,#dedede 48%,#f6f6f6 74%,#cacaca 100%);
    box-shadow:0 5px 4px -2px rgba(0,0,0,.45)}
  .page .deco{position:absolute;inset:0;width:100%;height:100%}
  .cover{left:218px;top:45px}
  .overview{left:73px;top:419px}
  .feature{left:362px;top:419px}
  .details{left:73px;top:791px}
  .back{left:362px;top:791px;background:var(--charcoal)}

  .photo{position:absolute;background:linear-gradient(180deg,#dfe3e7 0%,#c9ccd0 40%,#f1f1f1 60%,#9c9c94 100%)}
  .photo.interior{background:linear-gradient(160deg,#8a7a66 0%,#c5b49c 50%,#6f5b48 100%)}
  .photo.garage{background:linear-gradient(180deg,#d9d9d9 0%,#a8a8a8 55%,#5b5b5b 100%)}
  .photo.red-barn{background:linear-gradient(180deg,#b9cfe6 0%,#e6ecf2 30%,#a4302c 55%,#8c8c7a 100%)}

  /* cover */
  .cover .hero{left:0;top:160px;width:279px;height:201px}
  .cover-title{position:absolute;left:18px;top:42px;font-family:"Playfair Display",Georgia,serif;font-weight:900;font-size:26px;line-height:25px;color:var(--ink);letter-spacing:-.3px}
  .cover-sub{position:absolute;left:18px;top:119px;font-size:10.5px;line-height:13.5px;color:#2b2b2b}
  .brand{position:absolute;font-family:"Playfair Display",Georgia,serif;font-weight:900;color:var(--ink);text-align:center;line-height:1;white-space:nowrap}
  .cover .brand{left:180px;top:42px;width:92px;font-size:11.5px}
  .brand small{display:block;font-size:.62em;letter-spacing:1.2px;margin-top:2px}
  .cover-url{position:absolute;left:186px;top:68px;width:80px;text-align:center;font-size:5.5px}

  /* inner pages */
  .page-brand{left:10px;top:12px;width:52px;font-size:6px;color:var(--paper)}
  .page-brand small{letter-spacing:.6px}
  .page-heading{position:absolute;left:0;right:0;top:46px;text-align:center;font-family:"Playfair Display",Georgia,serif;font-weight:900;font-size:14px;letter-spacing:.3px;color:var(--ink)}
  .page-url{position:absolute;right:16px;top:344px;font-size:4.2px;color:var(--paper)}

  .category{position:absolute;left:0;width:279px;height:76px}
  .category .label{position:absolute;left:171px;top:20px;font-size:10.5px;line-height:14px;color:var(--paper)}
  .category .photo{left:28px;top:3px;width:129px;height:72px}

  .feature .main{left:28px;top:74px;width:222px;height:124px;border:2px solid var(--charcoal)}
  .lead{position:absolute;left:30px;right:30px;top:205px;text-align:center;font-size:5.4px;line-height:7px;color:var(--caption)}
  .thumb{position:absolute;top:230px;width:76px;height:56px;border:1px solid var(--frame);border-radius:0 0 9px 0}
  .thumb-caption{position:absolute;top:290px;width:76px;text-align:center;font-size:3.9px;line-height:5.2px;color:var(--caption)}

  .detail-photo{position:absolute;width:76px;height:56px;border:1px solid var(--paper);border-radius:8px 0 8px 0;box-shadow:0 1px 2px rgba(0,0,0,.3)}
  .detail-text{position:absolute;background:var(--charcoal);color:#f0f0f0;font-size:3.7px;line-height:5px;padding:6px 6px;overflow:hidden}

  /* back */
  .back .brand{left:80px;top:144px;width:120px;font-size:12.5px}
  .contact{position:absolute;left:0;right:0;text-align:center;font-size:5.6px;line-height:7px;color:var(--caption)}
  .contact-icon{position:absolute;left:134px;width:10px;height:10px}
</style>
</head>
<body>

<!-- Cover -->
<section class="page cover">
  <div class="photo hero" role="img" aria-label="Photo of a white two-storey post frame home with a wraparound deck and metal roof"></div>
  <svg class="deco" viewBox="0 0 279 361" aria-hidden="true">
    <defs>
      <linearGradient id="coverSteel" x1="0" y1="0" x2="1" y2="1">
        <stop offset="0" stop-color="#bdbdbd"/><stop offset=".45" stop-color="#ececec"/><stop offset="1" stop-color="#c4c4c4"/>
      </linearGradient>
      <linearGradient id="coverSteelDark" x1="0" y1="0" x2="1" y2="1">
        <stop offset="0" stop-color="#8e8e8e"/><stop offset=".5" stop-color="#d9d9d9"/><stop offset="1" stop-color="#b3b3b3"/>
      </linearGradient>
    </defs>
    <path d="M0 0H279V165C190 160 80 165 0 183Z" fill="url(#coverSteel)"/>
    <path d="M0 183C80 165 190 160 279 165" fill="none" stroke="#7d7d7d" stroke-width="3"/>
    <path d="M137 0H279V163C200 140 142 80 137 0Z" fill="url(#coverSteelDark)"/>
    <path d="M137 0C142 80 200 140 279 163" fill="none" stroke="#f4f4f4" stroke-width="4"/>
  </svg>
  <h1 class="cover-title">POST<br>FRAME<br>BUILDING</h1>
  <p class="cover-sub">Residential, Commercial<br>and other buildings</p>
  <div class="brand">HALVORSEN<small>BUILDERS, INC.</small></div>
  <p class="cover-url">www.loreum ipsum.com</p>
</section>

<!-- Overview -->
<section class="page overview">
  <svg class="deco" viewBox="0 0 279 361" aria-hidden="true">
    <path d="M0 0H279V2C200 8 100 28 0 36Z" fill="var(--charcoal)"/>
    <path d="M0 38C100 30 200 10 266 3" fill="none" stroke="#b5b5b5" stroke-width="1.5"/>
    <path d="M33 361C100 345 200 333 279 330V361Z" fill="var(--charcoal)"/>
    <path d="M28 361C100 342 200 329 279 327" fill="none" stroke="#b5b5b5" stroke-width="1.2"/>
    <g fill="var(--charcoal)">
      <path d="M88 80H259V119L235 135H157V80Z"/>
      <path d="M88 158H259V197L235 213H157V158Z"/>
      <path d="M88 236H259V275L235 291H157V236Z"/>
    </g>
  </svg>
  <div class="brand page-brand">HALVORSEN<small>BUILDERS, INC.</small></div>
  <h2 class="page-heading">HEADING</h2>

  <div class="category" style="top:80px">
    <div class="photo" role="img" aria-label="Photo of a white residential post frame house with a timber gable porch"></div>
    <svg class="deco" viewBox="0 0 279 76" aria-hidden="true"><path d="M28 58L55 75H28Z" fill="var(--charcoal)"/></svg>
    <p class="label">Residential<br>Buildings</p>
  </div>
  <div class="category" style="top:158px">
    <div class="photo" role="img" aria-label="Photo of a two-storey commercial post frame building with a balcony deck"></div>
    <svg class="deco" viewBox="0 0 279 76" aria-hidden="true"><path d="M28 58L55 75H28Z" fill="var(--charcoal)"/></svg>
    <p class="label">Commercial<br>Buildings</p>
  </div>
  <div class="category" style="top:236px">
    <div class="photo red-barn" role="img" aria-label="Photo of a red post frame garage with an open overhead door"></div>
    <svg class="deco" viewBox="0 0 279 76" aria-hidden="true"><path d="M28 58L55 75H28Z" fill="var(--charcoal)"/></svg>
    <p class="label">Other<br>Buildings</p>
  </div>

  <p class="page-url">www.loreum ipsum.com</p>
</section>

<!-- Feature -->
<section class="page feature">
  <svg class="deco" viewBox="0 0 279 361" aria-hidden="true">
    <path d="M0 0H279V2C200 8 100 28 0 36Z" fill="var(--charcoal)"/>
    <path d="M0 38C100 30 200 10 266 3" fill="none" stroke="#b5b5b5" stroke-width="1.5"/>
    <path d="M33 361C100 345 200 333 279 330V361Z" fill="var(--charcoal)"/>
    <path d="M28 361C100 342 200 329 279 327" fill="none" stroke="#b5b5b5" stroke-width="1.2"/>
  </svg>
  <div class="brand page-brand">HALVORSEN<small>BUILDERS, INC.</small></div>
  <h2 class="page-heading">HEADING</h2>
  <div class="photo main" role="img" aria-label="Photo of a white post frame home with a stone and timber front porch"></div>
  <p class="lead">Lorem ipsum dolor sit amet, consectetuer adipiscing elit, sed diam nonummy nibh euismod tincidunt ut laoreet dolore magna aliquam erat volutpat.</p>

  <div class="photo garage thumb" style="left:20px" role="img" aria-label="Photo of a garage interior with a utility vehicle and boat"></div>
  <div class="photo interior thumb" style="left:102px" role="img" aria-label="Photo of a kitchen interior with island and stainless appliances"></div>
  <div class="photo interior thumb" style="left:184px" role="img" aria-label="Photo of a living area with staircase and loft"></div>
  <p class="thumb-caption" style="left:20px">Lorem ipsum dolor sit amet, consectetuer adipiscing elit, sed diam nonummy nibh euismod tincidunt ut laoreet dolore magna aliquam erat volutpat.</p>
  <p class="thumb-caption" style="left:102px">Lorem ipsum dolor sit amet, consectetuer adipiscing elit, sed diam nonummy nibh euismod tincidunt ut laoreet dolore magna aliquam erat volutpat.</p>
  <p class="thumb-caption" style="left:184px">Lorem ipsum dolor sit amet, consectetuer adipiscing elit, sed diam nonummy nibh euismod tincidunt ut laoreet dolore magna aliquam erat volutpat.</p>

  <p class="page-url">www.loreum ipsum.com</p>
</section>

<!-- Details -->
<section class="page details">
  <svg class="deco" viewBox="0 0 279 361" aria-hidden="true">
    <path d="M0 0H279V2C200 8 100 28 0 36Z" fill="var(--charcoal)"/>
    <path d="M0 38C100 30 200 10 266 3" fill="none" stroke="#b5b5b5" stroke-width="1.5"/>
    <path d="M33 361C100 345 200 333 279 330V361Z" fill="var(--charcoal)"/>
    <path d="M28 361C100 342 200 329 279 327" fill="none" stroke="#b5b5b5" stroke-width="1.2"/>
  </svg>
  <div class="brand page-brand">HALVORSEN<small>BUILDERS, INC.</small></div>
  <h2 class="page-heading">HEADING</h2>

  <p class="detail-text" style="left:92px;top:76px;width:171px;height:42px">Lorem ipsum dolor sit amet, consectetuer adipiscing elit, sed diam nonummy nibh euismod tincidunt ut laoreet dolore magna aliquam erat volutpat. Ut wisi enim ad minim veniam, quis nostrud exerci tation ullamcorper suscipit lobortis nisl ut aliquip ex ea commodo consequat. Duis autem vel eum iriure dolor in hendrerit in vulputate velit esse molestie consequat.</p>
  <div class="photo garage detail-photo" style="left:16px;top:69px" role="img" aria-label="Photo of a garage interior with a utility vehicle and boat"></div>

  <p class="detail-text" style="left:16px;top:143px;width:171px;height:43px">Lorem ipsum dolor sit amet, consectetuer adipiscing elit, sed diam nonummy nibh euismod tincidunt ut laoreet dolore magna aliquam erat volutpat. Ut wisi enim ad minim veniam, quis nostrud exerci tation ullamcorper suscipit lobortis nisl ut aliquip ex ea commodo consequat. Duis autem vel eum iriure dolor in hendrerit in vulputate velit esse molestie consequat.</p>
  <div class="photo interior detail-photo" style="left:187px;top:134px" role="img" aria-label="Photo of a kitchen interior with island and stainless appliances"></div>

  <p class="detail-text" style="left:92px;top:204px;width:171px;height:43px">Lorem ipsum dolor sit amet, consectetuer adipiscing elit, sed diam nonummy nibh euismod tincidunt ut laoreet dolore magna aliquam erat volutpat. Ut wisi enim ad minim veniam, quis nostrud exerci tation ullamcorper suscipit lobortis nisl ut aliquip ex ea commodo consequat. Duis autem vel eum iriure dolor in hendrerit in vulputate velit esse molestie consequat.</p>
  <div class="photo interior detail-photo" style="left:16px;top:198px" role="img" aria-label="Photo of a living area with staircase and loft"></div>

  <p class="detail-text" style="left:16px;top:268px;width:171px;height:43px">Lorem ipsum dolor sit amet, consectetuer adipiscing elit, sed diam nonummy nibh euismod tincidunt ut laoreet dolore magna aliquam erat volutpat. Ut wisi enim ad minim veniam, quis nostrud exerci tation ullamcorper suscipit lobortis nisl ut aliquip ex ea commodo consequat. Duis autem vel eum iriure dolor in hendrerit in vulputate velit esse molestie consequat.</p>
  <div class="photo detail-photo" style="left:187px;top:262px" role="img" aria-label="Photo of a white and grey post frame shop building with a tall overhead door"></div>

  <p class="page-url">www.loreum ipsum.com</p>
</section>

<!-- Back cover -->
<section class="page back">
  <svg class="deco" viewBox="0 0 279 361" aria-hidden="true">
    <defs>
      <linearGradient id="backSteel" x1="0" y1="0" x2="1" y2="1">
        <stop offset="0" stop-color="#e6e6e6"/><stop offset=".5" stop-color="#c7c7c7"/><stop offset="1" stop-color="#ededed"/>
      </linearGradient>
    </defs>
    <path d="M0 68C90 72 200 100 279 127V308C190 274 100 252 0 230Z" fill="url(#backSteel)"/>
    <path d="M0 64C90 67 200 94 279 121" fill="none" stroke="#d8d8d8" stroke-width="2"/>
    <path d="M0 234C100 256 190 278 279 312" fill="none" stroke="#d8d8d8" stroke-width="2.5"/>
  </svg>
  <div class="brand">HALVORSEN<small>BUILDERS, INC.</small></div>

  <svg class="contact-icon" style="top:167px" viewBox="0 0 10 10" aria-hidden="true"><circle cx="5" cy="5" r="4.4" fill="none" stroke="#333" stroke-width=".6"/><path d="M5 2.4a1.7 1.7 0 0 1 1.7 1.7C6.7 5.4 5 7.4 5 7.4S3.3 5.4 3.3 4.1A1.7 1.7 0 0 1 5 2.4Z" fill="none" stroke="#333" stroke-width=".6"/></svg>
  <p class="contact" style="top:178px">Lorem ipsum dolor sit amet,<br>consectetuer adipiscing elit</p>

  <svg class="contact-icon" style="top:195px" viewBox="0 0 10 10" aria-hidden="true"><circle cx="5" cy="5" r="4.4" fill="none" stroke="#333" stroke-width=".6"/><path d="M3.4 3c.3-.3.6-.3.8 0l.5.7c.1.2 0 .4-.2.6l-.2.2c.3.6.7 1 1.3 1.3l.2-.2c.2-.2.4-.3.6-.2l.7.5c.3.2.3.5 0 .8-.6.6-1.7.3-2.8-.8S2.8 3.6 3.4 3Z" fill="#333"/></svg>
  <p class="contact" style="top:206px">0000-000-000</p>

  <svg class="contact-icon" style="top:216px" viewBox="0 0 10 10" aria-hidden="true"><circle cx="5" cy="5" r="4.4" fill="none" stroke="#333" stroke-width=".6"/><circle cx="5" cy="5" r="2.6" fill="none" stroke="#333" stroke-width=".5"/><path d="M2.4 5h5.2M5 2.4c-1 1.4-1 3.8 0 5.2M5 2.4c1 1.4 1 3.8 0 5.2" fill="none" stroke="#333" stroke-width=".4"/></svg>
  <p class="contact" style="top:227px">www.loreum ipsum.com</p>

  <svg class="contact-icon" style="top:237px" viewBox="0 0 10 10" aria-hidden="true"><circle cx="5" cy="5" r="4.4" fill="none" stroke="#333" stroke-width=".6"/><rect x="2.8" y="3.5" width="4.4" height="3" fill="#333"/><path d="M2.8 3.5 5 5.2 7.2 3.5" fill="none" stroke="#eee" stroke-width=".4"/></svg>
  <p class="contact" style="top:248px">info@loreum.ipsum.com</p>
</section>

</body>
</html>
```